Pegan Pyramid

Need a graphic for community lecture next week on preventing Cognitive Decline. Would like a Food Pyramid very similar to the one at this link, but with some adjustments:
1. Picture of "non-startchy veggie plant foods" might also include purple onion, garlic, purple cabbage, shitake mushrooms (in addition to what's pictured)
2. "Protein & Healthy Fats" would say "Mindful Protein & Healthy Fats". Picture should also include olive oil
3. Picture of starchy veggies would be more carrot/yam/beets/squash
http://www.dorvaleth.com/wellness/roots-and-greens-the-kitchen-plan-few-people-try/
Look forward to your design!!

```html
<!DOCTYPE html>
<html lang="en">
<head>
<meta charset="utf-8">
<title>Pegan Pyramid</title>
<link href="https://fonts.googleapis.com/css2?family=Bebas+Neue&display=swap" rel="stylesheet">
<style>
  :root {
    --sky: #29a8e0;
    --sky-deep: #1b7db6;
    --forest: #078a40;
    --forest-deep: #05602c;
    --lime: #8cc63f;
    --lime-deep: #5f9a28;
    --amber: #f8ac3c;
    --amber-deep: #d98a1f;
    --coral: #f76a36;
    --coral-deep: #d34e1d;
    --scarlet: #ee4037;
    --scarlet-deep: #c02a24;
    --title: #0b6b35;
    --ink-light: #ffffff;
  }
  html, body {
    margin: 0;
    padding: 0;
    width: 1200px;
    height: 938px;
    overflow: hidden;
    background: #ffffff;
  }
  .poster {
    display: block;
    width: 1200px;
    height: 938px;
  }
  .label {
    font-family: "Bebas Neue", "Oswald", sans-serif;
    fill: var(--ink-light);
    font-size: 33px;
    letter-spacing: 0.5px;
  }
  .title {
    font-family: "Bebas Neue", "Oswald", sans-serif;
    fill: var(--title);
    font-size: 124px;
    letter-spacing: 3px;
  }
</style>
</head>
<body>
<svg class="poster" viewBox="0 0 1478 1158" width="1200" height="938" preserveAspectRatio="none" xmlns="http://www.w3.org/2000/svg">
  <defs>
    <linearGradient id="produce-wash" x1="0" y1="0" x2="1" y2="1">
      <stop offset="0" stop-color="#e6eedd"/>
      <stop offset="0.35" stop-color="#f2ead9"/>
      <stop offset="0.65" stop-color="#e3ecd6"/>
      <stop offset="1" stop-color="#f1e3dc"/>
    </linearGradient>
  </defs>

  <!-- Background wash -->
  <rect class="backdrop" role="img" aria-label="Faded photograph of assorted fresh vegetables: melons, squash, peppers, cabbage and eggplant" x="0" y="0" width="1478" height="1158" fill="url(#produce-wash)"/>

  <!-- Tier 1: sparingly -->
  <g class="tier tier--treats">
    <polygon points="72,66 771,66 711,196 72,196" fill="var(--sky-deep)"/>
    <polygon points="66,60 765,60 705,190 66,190" fill="var(--sky)"/>
    <text class="label" x="390" y="137" text-anchor="middle">SPARINGLY</text>
    <polygon points="806,66 941,66 1009,204 756,204" fill="var(--sky-deep)"/>
    <polygon points="800,60 935,60 1003,198 750,198" fill="var(--sky)"/>
    <g role="img" aria-label="Bottles of whiskey and slices of layered cake">
      <rect x="800" y="50" width="140" height="100" rx="14" fill="#b56a3a" opacity="0.85"/>
    </g>
    <text class="label" x="870" y="183" text-anchor="middle" font-size="27">RECREATIONAL TREATS</text>
  </g>

  <!-- Tier 2: spices and herbs -->
  <g class="tier tier--spices">
    <polygon points="72,226 686,226 626,358 72,358" fill="var(--forest-deep)"/>
    <polygon points="66,220 680,220 620,352 66,352" fill="var(--forest)"/>
    <text class="label" x="358" y="298" text-anchor="middle">UNLIMITED AMOUNTS</text>
    <polygon points="716,226 1041,226 1091,364 673,364" fill="var(--forest-deep)"/>
    <polygon points="710,220 1035,220 1085,358 667,358" fill="var(--forest)"/>
    <g role="img" aria-label="Peppercorns, spice grinder, cinnamon sticks, star anise, chili and ground spices">
      <ellipse cx="820" cy="283" rx="108" ry="62" fill="#a8543a" opacity="0.8"/>
    </g>
    <text class="label" x="968" y="266" text-anchor="middle">SPICES</text>
    <text class="label" x="968" y="304" text-anchor="middle">AND</text>
    <text class="label" x="968" y="342" text-anchor="middle">HERBS</text>
  </g>

  <!-- Tier 3: beans and grains -->
  <g class="tier tier--legumes">
    <polygon points="72,388 606,388 546,526 72,526" fill="var(--lime-deep)"/>
    <polygon points="66,382 600,382 540,520 66,520" fill="var(--lime)"/>
    <text class="label" x="296" y="421" text-anchor="middle">INCLUDE UP TO 1/2 CUP OF</text>
    <text class="label" x="296" y="459" text-anchor="middle">GLUTEN FREE GRAINS, UP TO 1/2</text>
    <text class="label" x="296" y="497" text-anchor="middle">CUP-1 CUP OF BEANS</text>
    <polygon points="636,388 1116,388 1174,528 591,528" fill="var(--lime-deep)"/>
    <polygon points="630,382 1110,382 1168,522 585,522" fill="var(--lime)"/>
    <g role="img" aria-label="Assorted dried beans, chickpeas, lentils, corn and seeds in a heap">
      <ellipse cx="755" cy="440" rx="125" ry="64" fill="#9a6a4a" opacity="0.85"/>
    </g>
    <text class="label" x="996" y="443" text-anchor="middle">BEANS, LEGUMES,</text>
    <text class="label" x="996" y="481" text-anchor="middle">NON GLUTEN GRAINS</text>
  </g>

  <!-- Tier 4: fruits and starchy veggies -->
  <g class="tier tier--fruit-starch">
    <polygon points="72,548 526,548 461,686 72,686" fill="var(--amber-deep)"/>
    <polygon points="66,542 520,542 455,680 66,680" fill="var(--amber)"/>
    <text class="label" x="268" y="580" text-anchor="middle">FOCUS ON LOW GLYCEMIC FRUIT</text>
    <text class="label" x="268" y="618" text-anchor="middle">(1 CUP PER DAY) &amp; UP TO 2 SERVINGS</text>
    <text class="label" x="268" y="656" text-anchor="middle">OF STARCHY VEGGIES PER DAY</text>
    <polygon points="561,548 871,548 871,686 508,686" fill="var(--amber-deep)"/>
    <polygon points="555,542 865,542 865,680 502,680" fill="var(--amber)"/>
    <g role="img" aria-label="Basket of fruit with watermelon, pineapple, grapes, oranges, pears and kiwi">
      <ellipse cx="652" cy="608" rx="105" ry="68" fill="#c9472c" opacity="0.75"/>
    </g>
    <text class="label" x="805" y="619" text-anchor="middle">FRUITS</text>
    <polygon points="884,548 1201,548 1256,686 884,686" fill="var(--amber-deep)"/>
    <polygon points="878,542 1195,542 1250,680 878,680" fill="var(--amber)"/>
    <g role="img" aria-label="Sweet potatoes, carrots, beets and squash">
      <ellipse cx="982" cy="608" rx="98" ry="62" fill="#e06a2c" opacity="0.8"/>
    </g>
    <text class="label" x="1132" y="605" text-anchor="middle">STARCHY</text>
    <text class="label" x="1132" y="643" text-anchor="middle">VEGGIES</text>
  </g>

  <!-- Tier 5: protein and fats -->
  <g class="tier tier--protein">
    <polygon points="72,708 444,708 381,846 72,846" fill="var(--coral-deep)"/>
    <polygon points="66,702 438,702 375,840 66,840" fill="var(--coral)"/>
    <text class="label" x="236" y="745" text-anchor="middle">4-6 OZ OF PROTEIN</text>
    <text class="label" x="236" y="783" text-anchor="middle">PER MEAL, &amp; 3-5 SERVINGS</text>
    <text class="label" x="236" y="821" text-anchor="middle">OF FAT PER DAY</text>
    <polygon points="476,708 1271,708 1339,846 426,846" fill="var(--coral-deep)"/>
    <polygon points="470,702 1265,702 1333,840 420,840" fill="var(--coral)"/>
    <g role="img" aria-label="Raw beef, whole fish, salmon steak, eggs, nuts and beans">
      <ellipse cx="610" cy="768" rx="100" ry="66" fill="#b8503a" opacity="0.85"/>
    </g>
    <text class="label" x="828" y="762" text-anchor="middle">MINDFUL PROTEIN</text>
    <text class="label" x="828" y="800" text-anchor="middle">&amp; HEALTHY FATS</text>
    <g role="img" aria-label="Olive oil bottle, olives, mixed nuts and a halved avocado">
      <ellipse cx="1112" cy="768" rx="148" ry="64" fill="#7f8a2e" opacity="0.8"/>
    </g>
  </g>

  <!-- Tier 6: non-starchy veggies -->
  <g class="tier tier--veggies">
    <polygon points="72,868 361,868 296,1008 72,1008" fill="var(--scarlet-deep)"/>
    <polygon points="66,862 355,862 290,1002 66,1002" fill="var(--scarlet)"/>
    <text class="label" x="196" y="918" text-anchor="middle">UNLIMITED</text>
    <text class="label" x="196" y="956" text-anchor="middle">AMOUNTS</text>
    <polygon points="401,868 1351,868 1424,1006 341,1006" fill="var(--scarlet-deep)"/>
    <polygon points="395,862 1345,862 1418,1000 335,1000" fill="var(--scarlet)"/>
    <g role="img" aria-label="Pile of leafy greens, broccoli, eggplant, peppers, tomatoes, cabbage, onion and mushrooms">
      <ellipse cx="556" cy="928" rx="142" ry="66" fill="#5f8a32" opacity="0.85"/>
    </g>
    <text class="label" x="860" y="923" text-anchor="middle">NON-STARTCHY</text>
    <text class="label" x="860" y="961" text-anchor="middle">VEGGIE PLANT FOODS</text>
    <g role="img" aria-label="Pile of leafy greens, broccoli, eggplant, peppers, tomatoes, cabbage, onion and mushrooms">
      <ellipse cx="1180" cy="928" rx="142" ry="66" fill="#5f8a32" opacity="0.85"/>
    </g>
  </g>

  <text class="title" x="745" y="1118" text-anchor="middle">PEGAN PYRAMID</text>
</svg>
</body>
</html>
```